Commit to H.E.A.L. (Healthy Eating and Living)Corporate Wellness

Pledge to R.O.O.T. (Renewed Outlook On Thriving) is my health and wellness company. I am a certified Health & Lifestyle Coach who provides a 6 month one-on-one coaching program for individuals and groups. I also provide 1 hour health seminars or "brown bag" lunches for any type of organization. My focus is on prevention of chronic disease through health and food education, as well as effective lifestyle coaching. I would like the brochure to have my logo, my name and certification, some health statistics, and my programs/seminars. Looking for a one page, half fold or trifold brochure design. I am flexible! I forgot to include my personal information. phone number 614/352-8807. email is marla@vibrantroutinesproject.com. website is www.pledgetoroot.com.

Target Market(s)

Companies (large or small) looking for wellness and disease prevention programs for their employees.

Industry/Entity Type

Health

Requirements
Must have
• I am going into this with no picture in my head as to what I want. I like simplicity. I like to represent health, in all aspects, from food to environment. I will attach my logo to use, and colors should accent the logo.
I need it to include my name and title (Marla Quistwood, Certified Health & Lifestyle Coach). The tag line "Because your employee's health IS your business." These statistics listed clearly: "1. The U.S. spends $2.8 trillion on health care every year, and this number is rising. 2. Treating individuals with chronic preventable disease is responsible for 75% of our health care costs. 3. The U.S. spends more on healthcare than Japan, Germany, France, China, UK, Italy, Canada, Brazil, Spain and Australia COMBINED. 4. The Global Vitality Council ranks the U.S. 37th for overall health outcomes. This means that more healthcare spending does not equate to better health.
Then it needs to say that "Our healthcare costs are out of control, increasing, and unsustainable. We do not have a healthcare system, we have a disease care system. Prevention of chronic disease is the only way to reduce our costs. Workplace wellness solutions MUST change behaviors. Food and health education, as well as effective lifestyle coaching are the keys to this behavior change."
I offer 1 hour seminars, sample seminars include but are not limited to "Guarding Your Cells" "Plates of the Nation/Ills of the Nation," and "Vitality & Balance start when Old Habits Stop." I also offer a six month bi-weekly health coaching program for individuals or small groups. Plus custom programs that include health food store tours, pantry purges, cooking ideas and preparation, etc.

```html
<!DOCTYPE html>
<html lang="en">
<head>
<meta charset="utf-8">
<title>Pledge to R.O.O.T. — Brochure Cover</title>
<link rel="stylesheet" href="https://fonts.googleapis.com/css2?family=Anton&family=Arimo:wght@400;700&family=Quattrocento:wght@400;700&family=Roboto+Condensed:wght@700&display=swap">
<style>
  :root {
    --lime: #e3ef5c;
    --leaf: #a8c928;
    --forest: #5e8e0c;
    --white: #ffffff;
    --cap-top: #ffffff;
    --cap-bottom: #dcdcdc;
    --mark-green: #6f9a25;
    --mark-faint: rgba(110, 140, 40, 0.35);
    --shadow: rgba(40, 60, 0, 0.55);
  }
  * { margin: 0; padding: 0; box-sizing: border-box; }
  html, body { width: 1200px; height: 848px; overflow: hidden; background: #ffffff; }
  .brochure {
    position: relative;
    width: 1200px;
    height: 848px;
    overflow: hidden;
    background: linear-gradient(160deg, var(--lime) 0%, var(--leaf) 45%, var(--forest) 100%);
    font-family: "Arimo", Arial, sans-serif;
    color: var(--white);
  }
  .back-panel { position: absolute; left: 0; top: 0; width: 605px; height: 848px; }
  .front-panel { position: absolute; left: 605px; top: 0; width: 595px; height: 848px; }

  .brand-cap { position: absolute; left: 0; top: 0; width: 595px; height: 220px; }
  .brand-cap svg { position: absolute; inset: 0; }
  .brand-mark {
    position: absolute; left: 0; right: 0; top: 118px;
    display: flex; align-items: center; justify-content: center; gap: 12px;
    font-family: "Arimo", Arial, sans-serif; font-weight: 700;
    font-size: 26px; color: var(--mark-green); letter-spacing: 0.5px;
  }
  .brand-dot { width: 22px; height: 22px; border-radius: 50%; background: var(--mark-green); }

  .brand-ghost {
    position: absolute; left: 30px; top: 370px; width: 520px;
    display: flex; align-items: center; gap: 16px;
    font-family: "Arimo", Arial, sans-serif; font-weight: 700;
    font-size: 40px; color: var(--mark-faint);
  }
  .brand-ghost .brand-dot { width: 36px; height: 36px; background: var(--mark-faint); }

  .cover-title {
    position: absolute; left: 0; right: 0; top: 405px; text-align: center;
    font-family: "Anton", Impact, sans-serif; font-size: 104px; line-height: 1;
    letter-spacing: 6px; color: var(--white);
    text-shadow: 2px 3px 4px var(--shadow);
  }
  .cover-subtitle {
    position: absolute; left: 0; right: 0; top: 527px; text-align: center;
    font-size: 31px; letter-spacing: 3px; word-spacing: 10px; color: var(--white);
    text-shadow: 1px 1px 2px var(--shadow);
  }

  .coach { position: absolute; left: 60px; width: 440px; top: 536px; text-align: center; }
  .coach-name {
    font-family: "Anton", Impact, sans-serif; font-size: 36px; letter-spacing: 2px;
    line-height: 1.1; text-shadow: 2px 2px 3px var(--shadow);
  }
  .coach-title {
    font-family: "Quattrocento", Georgia, serif; font-weight: 700; font-size: 15px;
    letter-spacing: 2.5px; margin-top: 4px; text-shadow: 1px 1px 2px var(--shadow);
  }
  .coach-tagline {
    font-family: "Quattrocento", Georgia, serif; font-size: 15px; letter-spacing: 0.5px;
    margin-top: 2px; text-shadow: 1px 1px 2px var(--shadow);
  }

  .contact-list { position: absolute; left: 80px; top: 645px; list-style: none; }
  .contact-item {
    display: flex; align-items: center; gap: 14px;
    font-family: "Roboto Condensed", "Arial Narrow", sans-serif; font-weight: 700;
    color: var(--white); text-shadow: 2px 2px 3px var(--shadow);
  }
  .contact-item svg { flex: none; filter: drop-shadow(2px 2px 2px var(--shadow)); }
  .contact-phone { font-size: 40px; height: 60px; }
  .contact-email { font-size: 19px; letter-spacing: 1px; height: 60px; margin-top: 10px; }
  .contact-web { font-size: 25px; letter-spacing: 1px; height: 60px; margin-top: 4px; }
</style>
</head>
<body>
<main class="brochure">
  <section class="back-panel">
    <div class="brand-ghost"><span class="brand-dot"></span>Pledge to R.O.O.T.</div>

    <div class="coach">
      <h2 class="coach-name">Marla Quistwood</h2>
      <p class="coach-title">Certified Health &amp; Lifestyle Coach</p>
      <p class="coach-tagline">(Because your employee's health IS your business)</p>
    </div>

    <ul class="contact-list">
      <li class="contact-item contact-phone">
        <svg width="52" height="52" viewBox="0 0 52 52" aria-hidden="true">
          <path d="M14 4c4 0 6 8 6 11s-4 4-4 7 7 13 11 14 4-4 8-4 11 3 11 7-6 9-10 9C21 48 4 31 4 14 4 9 10 4 14 4z" fill="none" stroke="#ffffff" stroke-width="4" stroke-linejoin="round"/>
        </svg>
        <span>- 614/352-8807</span>
      </li>
      <li class="contact-item contact-email">
        <svg width="44" height="44" viewBox="0 0 44 44" aria-hidden="true">
          <circle cx="22" cy="22" r="8" fill="none" stroke="#ffffff" stroke-width="4"/>
          <path d="M30 14v11c0 5 8 5 8-3A16 16 0 1 0 30 36" fill="none" stroke="#ffffff" stroke-width="4" stroke-linecap="round"/>
        </svg>
        <span>marla@vibrantroutinesproject.com</span>
      </li>
      <li class="contact-item contact-web">
        <svg width="44" height="44" viewBox="0 0 44 44" aria-hidden="true">
          <circle cx="22" cy="22" r="18" fill="none" stroke="#ffffff" stroke-width="3.5"/>
          <ellipse cx="22" cy="22" rx="8" ry="18" fill="none" stroke="#ffffff" stroke-width="3"/>
          <path d="M4 22h36M8 12h28M8 32h28" stroke="#ffffff" stroke-width="3"/>
        </svg>
        <span>www.pledgetoroot.com</span>
      </li>
    </ul>
  </section>

  <section class="front-panel">
    <div class="brand-cap">
      <svg width="595" height="220" viewBox="0 0 595 220" aria-hidden="true">
        <defs>
          <linearGradient id="capFill" x1="0" y1="0" x2="0" y2="1">
            <stop offset="0" stop-color="#ffffff"/>
            <stop offset="0.55" stop-color="#f7f7f7"/>
            <stop offset="1" stop-color="#d8d8d8"/>
          </linearGradient>
        </defs>
        <path d="M0 0H595V178C520 210 420 218 310 214 180 210 70 190 0 138Z" fill="url(#capFill)" stroke="#ffffff" stroke-width="3"/>
      </svg>
      <div class="brand-mark"><span class="brand-dot"></span>Pledge to R.O.O.T.</div>
    </div>

    <h1 class="cover-title">R.O.O.T.</h1>
    <p class="cover-subtitle">(Renewed Outlook On Thriving)</p>
  </section>
</main>
</body>
</html>
```